'WILD' eye catching Business Card Design / Logo for production company / TV host / adventurer

Hi there,

We are looking for a 'WILD' and exciting logo and double sided business card for our business "Bright Harbor Studios".

Marcus Thorley is an international television host, adventurer, author and inspirational public speaker.

We want to project Marcus' talents onto his business card.

We are looking for a business card design that can carry over onto letter heads, emails etc. We want a design that is 'WILD', different and exciting.

Feel free to check out Marcus' web site: www.brightharborstudios.example.nz to get a better understanding what he is about.

Please feel free to go completely 'WILD' on this project as we want something different with lots of WOW factors.

Thank you so much and we look forward to your designs.

We have a feeling that there will be many more designs in the near future.

Best regards,

the production team

We have added another task to the list.

If the winning designer can also provide us with a matching letterhead and email signature based on the same style of design as the business card.

Target Market(s)

People with passion.

Industry/Entity Type

Business

Requirements
Must have
• Bright Harbor Studios
Marcus Thorley
42 Ferndale Lane
Oakbridge 7420
New Zealand

Phone +64-(0)3-5527 046
Cell +64-(0)274-615 238

email: brightharbornz@example.com
www.brightharborstuios.example.nz
Nice to have
• A feature made out of the name 'Bright Harbor Studios'.

Marcus Thorley's name reasonably obvious.

All other details (except web site) can be quite small.

```html
<!DOCTYPE html>
<html lang="en">
<head>
<meta charset="utf-8">
<title>Bright Harbor Studios – Business Card</title>
<link href="https://fonts.googleapis.com/css2?family=Ubuntu:wght@500;700&family=Caveat:wght@500&display=swap" rel="stylesheet">
<style>
  :root {
    --backdrop: #953622;
    --paper-light: #fbe6a6;
    --paper-mid: #f3cf7c;
    --paper-deep: #e6ad5a;
    --ink-dark: #3b2616;
    --ink-rust: #8e3418;
    --claw: #8a6a6e;
    --label: #fdf1bf;
    --torn: #ffffff;
  }
  * { margin: 0; padding: 0; box-sizing: border-box; }
  html, body { width: 1200px; height: 897px; overflow: hidden; }
  body {
    background: var(--backdrop);
    font-family: "Ubuntu", Arial, sans-serif;
    position: relative;
  }
  .card {
    position: absolute;
    overflow: hidden;
    background:
      linear-gradient(160deg, rgba(255,255,255,0.25) 0%, rgba(255,255,255,0) 45%),
      radial-gradient(ellipse at 70% 80%, var(--paper-deep) 0%, rgba(230,173,90,0) 60%),
      linear-gradient(135deg, var(--paper-light) 0%, var(--paper-mid) 55%, var(--paper-deep) 100%);
  }
  .card--front { left: 110px; top: 77px; width: 588px; height: 370px; }
  .card--back  { left: 474px; top: 460px; width: 592px; height: 374px; }

  .paper-texture {
    position: absolute; inset: 0;
    background: linear-gradient(20deg, rgba(233,176,92,0.35) 0%, rgba(251,230,166,0) 60%);
  }

  .brand-name {
    position: absolute;
    font-weight: 700;
    color: var(--ink-rust);
    font-size: 33px;
    letter-spacing: 0.3px;
    line-height: 40px;
    white-space: nowrap;
  }
  .card--front .brand-name { left: 108px; top: 152px; }
  .card--back  .brand-name { left: 118px; top: 48px; }

  .address {
    position: absolute;
    left: 195px; top: 211px;
    width: 200px;
    text-align: center;
    color: var(--ink-dark);
    font-weight: 700;
    font-size: 13.5px;
    line-height: 18px;
  }
  .website {
    position: absolute;
    left: 136px; top: 332px;
    width: 300px;
    text-align: center;
    color: var(--ink-rust);
    font-weight: 700;
    font-size: 13px;
    white-space: nowrap;
  }

  .claw-marks {
    position: absolute;
    background: linear-gradient(180deg, rgba(138,106,110,0) 0%, rgba(138,106,110,0.45) 100%);
  }
  .card--front .claw-marks { left: 446px; top: 256px; width: 62px; height: 114px; }
  .card--back  .claw-marks { left: 508px; top: 218px; width: 84px; height: 102px; }

  .stamp {
    position: absolute;
    left: 4px; top: 115px; width: 96px; height: 96px;
  }

  .name-label {
    position: absolute;
    left: 102px; top: 130px;
    width: 384px; height: 120px;
    background: linear-gradient(180deg, var(--label) 0%, #f8e39e 100%);
    box-shadow: 0 2px 6px rgba(120,70,20,0.25);
  }
  .person-name {
    position: absolute;
    left: 46px; top: 20px;
    font-size: 20px; font-weight: 700;
    color: var(--ink-rust);
  }
  .person-roles {
    position: absolute;
    left: 46px; top: 53px;
    font-size: 12px; font-weight: 700;
    line-height: 18px;
    color: var(--ink-dark);
  }
  .person-roles .accent { color: var(--ink-rust); }
  .email {
    position: absolute;
    right: 6px; top: 84px;
    font-family: "Caveat", cursive;
    font-size: 17px;
    color: var(--ink-dark);
    transform: rotate(-6deg);
    white-space: nowrap;
  }
  .torn-edge {
    position: absolute;
    left: 102px; top: 248px;
    width: 230px; height: 14px;
  }
  .phones {
    position: absolute;
    left: 148px; top: 298px;
    font-size: 12.5px; font-weight: 700;
    line-height: 18px;
    color: var(--ink-dark);
  }
  .phones .prefix { color: var(--ink-rust); }
</style>
</head>
<body>

<section class="card card--front" aria-label="Business card front">
  <div class="paper-texture" role="img" aria-label="Weathered parchment texture"></div>
  <div class="brand-name">Bright Harbor Studios</div>
  <div class="address">
    42 Ferndale Lane<br>
    Oakbridge 7420<br>
    New Zealand
  </div>
  <div class="website">www.brightharborstudios.example.nz</div>
  <div class="claw-marks" role="img" aria-label="Animal claw scratch marks"></div>
</section>

<section class="card card--back" aria-label="Business card back">
  <div class="paper-texture" role="img" aria-label="Weathered parchment texture"></div>
  <div class="brand-name">Bright Harbor Studios</div>
  <svg class="stamp" viewBox="0 0 96 96" aria-hidden="true">
    <circle cx="48" cy="48" r="44" fill="none" stroke="var(--ink-rust)" stroke-width="2" opacity="0.3"/>
    <circle cx="48" cy="48" r="34" fill="none" stroke="var(--ink-rust)" stroke-width="1.5" opacity="0.25"/>
  </svg>
  <div class="name-label">
    <div class="person-name">Marcus Thorley</div>
    <div class="person-roles">
      <span class="accent">international</span> television host, <span class="accent">adventurer</span><br>
      <span class="accent">author, inspirational</span> public speaker
    </div>
    <div class="email">brightharbornz@example.com</div>
  </div>
  <svg class="torn-edge" viewBox="0 0 230 14" preserveAspectRatio="none" aria-hidden="true">
    <polyline points="0,0 230,0 230,6 200,10 170,5 140,11 110,6 80,12 50,6 20,11 0,7" fill="var(--torn)"/>
  </svg>
  <div class="phones">
    <span class="prefix">+64</span>-(0)3-5527 046<br>
    <span class="prefix">+64</span>-(0)274-615 238
  </div>
  <div class="claw-marks" role="img" aria-label="Animal claw scratch marks"></div>
</section>

</body>
</html>
```